500ml Aluminium drinking Water Bottle. Endlessly reusable and refillable

We need a label for our new 500ml water bottle. We are Corrie Vale Springs based in the Scottish Highlands. We extract filter and bottle drinking water from Loch Ness in Scotland. We currently have on the market a 100ml bottle of water designed for whisky drinkers see - www.fernhollowaqua.example
We now want to create a 500ml bottle of still and sparkling water using aluminium bottles which allows us much more room for branding. Our water will be exclusive and high end, not available in the supermarkets only selected outlets. Our current branding is based on the the number 126 which relates to the depth of the Loch at 126 Fathoms. We have interwound the legendary loch ness monster into the top half of the numbers. We will use the 126 logo on our new 500ml product but need a creative approach as to how it is presented on the bottle. Our 100ml Dew for Drams" product will stand alone, our new 500ml will use the same 126 logo, but its strap line will be changed to differentiate between our products. We need to maximise the available space on the aluminium bottle to ensure our product leaps out at the consumer. The available space for the new branding is 207mm wide x 120mm high, but in this space we need allow room for our barcode, address and statutory information, but we can scale these up or down. Our new design will be exclusive and elegant, not loud or harsh. It will represent a unique drinking water product from an iconic water source. So the branding of 126 is supplied. Our target consumer is middle aged and above with a disposable income,, those who want to experience rare and exclusive products and who are prepared to pay for that luxury.
Updates

Hi Guys - please fee free to use the 126 logo, but leave out "Dew for Drams". We are trying to create a label for 500ml aluminium bottles of still and sparkling drinking water for any occasion. We need the label design to be bold and vibrant but not brash or harsh. We are targeting exclusive retail and high end dining outlets, where the consumer will appreciate the pure water from the Scottish highlands. The history and scenery of Scotland should provide some inspiration for your designs or colour palette. We want to invoke thoughts of cold clear water and the refreshing taste of our pure water.

Target Market(s)

Exclusive high end consumers

Industry/Entity Type

food and drink

Requirements
Must have
• clear bright color scheme clever positioning of the logo
Should not have
• the term "Loch Ness Water" must not appear

```html
<!DOCTYPE html>
<html lang="en">
<head>
<meta charset="utf-8">
<title>Corrie Vale Springs – 500ml Labels</title>
<link rel="stylesheet" href="https://fonts.googleapis.com/css2?family=Montserrat:wght@400;500;700&display=swap">
<style>
  :root {
    --page-bg: #eef2f4;
    --label-top: #f4f5f6;
    --still-ink: #2a5f93;
    --still-deep: #4fb8d4;
    --still-mid: #d6ecf3;
    --spark-ink: #2f9e97;
    --spark-deep: #63c6b6;
    --spark-mid: #d9f0ec;
  }
  * { margin: 0; padding: 0; box-sizing: border-box; }
  html, body {
    width: 1200px; height: 1200px; overflow: hidden;
    background: var(--page-bg);
    font-family: "Montserrat", Arial, sans-serif;
  }
  .range {
    position: absolute; inset: 0;
    display: flex; justify-content: center; align-items: center; gap: 80px;
  }
  .label {
    position: relative;
    width: 460px; height: 1000px;
    border-radius: 24px;
    overflow: hidden;
    box-shadow: 0 10px 30px rgba(30, 60, 80, 0.12);
  }
  .label--still {
    color: var(--still-ink);
    background: linear-gradient(to bottom, var(--label-top) 0%, var(--label-top) 45%, var(--still-mid) 72%, var(--still-deep) 100%);
  }
  .label--sparkling {
    color: var(--spark-ink);
    background: linear-gradient(to bottom, var(--label-top) 0%, var(--label-top) 45%, var(--spark-mid) 72%, var(--spark-deep) 100%);
  }
  .tagline-band {
    position: absolute; left: 0; right: 0; top: 250px;
    height: 40px;
    border-top: 3px solid currentColor;
    border-bottom: 3px solid currentColor;
    display: flex; align-items: center; justify-content: center;
    font-size: 17px; font-weight: 500; letter-spacing: 3px;
    white-space: nowrap;
  }
  .tagline-side {
    position: absolute; left: 20px; top: 290px;
    height: 320px; width: 36px;
    border-right: 3px solid currentColor;
    display: flex; align-items: center; justify-content: center;
  }
  .tagline-side span {
    writing-mode: vertical-rl;
    font-size: 17px; font-weight: 500; letter-spacing: 3px;
    white-space: nowrap;
  }
  .seal {
    position: absolute; left: -22px; top: 360px;
    width: 44px; height: 60px;
    border: 3px solid currentColor; border-radius: 50%;
  }
  .label--sparkling .seal { display: none; }
  .front {
    position: absolute; left: 70px; right: 30px; top: 330px;
  }
  .brand {
    font-size: 44px; font-weight: 500; line-height: 1; letter-spacing: 1px;
    margin-bottom: 26px;
  }
  .pure {
    font-size: 46px; font-weight: 700; line-height: 1.05; letter-spacing: 1px;
  }
  .origin {
    font-size: 46px; font-weight: 400; line-height: 1.15; letter-spacing: 1px;
  }
  .volume {
    display: flex; align-items: center; gap: 28px;
    margin-top: 22px;
    font-size: 20px; font-weight: 500; letter-spacing: 1px;
  }
  .volume svg { display: block; }
</style>
</head>
<body>
  <main class="range">

    <section class="label label--still" aria-label="Still water label">
      <div class="tagline-band">N DEEP • STILL WATERS RUN DEEP • STILL WATERS RU</div>
      <div class="seal" aria-hidden="true"></div>
      <div class="front">
        <p class="brand">Corrie Vale</p>
        <p class="pure">PURE</p>
        <p class="origin">HIGHLAND<br>WATER</p>
        <div class="volume">
          <span>500ml</span>
          <svg width="220" height="14" viewBox="0 0 220 14" aria-hidden="true">
            <g stroke="currentColor" stroke-width="3">
              <line x1="2" y1="14" x2="10" y2="0"/><line x1="12" y1="14" x2="20" y2="0"/>
              <line x1="22" y1="14" x2="30" y2="0"/><line x1="32" y1="14" x2="40" y2="0"/>
              <line x1="42" y1="14" x2="50" y2="0"/><line x1="52" y1="14" x2="60" y2="0"/>
              <line x1="62" y1="14" x2="70" y2="0"/><line x1="72" y1="14" x2="80" y2="0"/>
            </g>
            <polygon points="86,14 94,0 220,0 220,14" fill="currentColor"/>
          </svg>
        </div>
      </div>
    </section>

    <section class="label label--sparkling" aria-label="Sparkling water label">
      <div class="tagline-side"><span>SOFT SPARKLING WATER •</span></div>
      <div class="front">
        <p class="brand">Corrie Vale</p>
        <p class="pure">PURE</p>
        <p class="origin">HIGHLAND<br>WATER</p>
        <div class="volume">
          <span>500ml</span>
          <svg width="220" height="14" viewBox="0 0 220 14" aria-hidden="true">
            <g stroke="currentColor" stroke-width="3">
              <line x1="2" y1="14" x2="10" y2="0"/><line x1="12" y1="14" x2="20" y2="0"/>
              <line x1="22" y1="14" x2="30" y2="0"/><line x1="32" y1="14" x2="40" y2="0"/>
              <line x1="42" y1="14" x2="50" y2="0"/><line x1="52" y1="14" x2="60" y2="0"/>
              <line x1="62" y1="14" x2="70" y2="0"/><line x1="72" y1="14" x2="80" y2="0"/>
            </g>
            <polygon points="86,14 94,0 220,0 220,14" fill="currentColor"/>
          </svg>
        </div>
      </div>
    </section>

  </main>
</body>
</html>
```